Tech business card design

We need an amazing business card design for our new business 'Vantry' a marketing tech startup based in Sydney, Australia. We provide an online marketplace for businesses to search and buy advertising media, connect with service providers and learn more about marketing. We wish to communicate 'cool tech', reliability and professionalism and design based around our logo.

Target Market(s)

Business Owners

Contact Information for Business Card

Name
Position
Email Address
Website
Phone Number

Font styles to use
Other font styles liked:
• Avenir & Avenir Next

Colors

Designer to choose colors to be used in the design.

```html
<!DOCTYPE html>
<html lang="en">
<head>
<meta charset="utf-8">
<title>Vantry Business Card</title>
<link rel="stylesheet" href="https://fonts.googleapis.com/css2?family=Nunito+Sans:wght@400;600;800&display=swap">
<style>
  :root {
    --navy: #141c48;
    --navy-deep: #0f1538;
    --navy-soft: #1c2657;
    --ink: #1a1a1a;
    --paper: #ffffff;
    --line-grey: #eef0f3;
    --stage: #e4e5e7;
  }
  * { margin: 0; padding: 0; box-sizing: border-box; }
  html, body { width: 1200px; height: 900px; overflow: hidden; }
  body {
    background: var(--stage);
    font-family: "Nunito Sans", sans-serif;
    position: relative;
  }
  .card {
    position: absolute;
    width: 600px;
    height: 343px;
    box-shadow: 0 6px 18px rgba(0,0,0,0.18);
    overflow: hidden;
  }
  /* Back side */
  .card-back {
    left: 300px;
    top: 60px;
    background: var(--navy);
  }
  .back-pattern {
    position: absolute;
    inset: 0;
    background: linear-gradient(135deg, var(--navy-soft), var(--navy-deep));
  }
  .back-wordmark {
    position: absolute;
    left: 0; right: 0; top: 50%;
    transform: translateY(-50%);
    text-align: center;
    color: var(--paper);
    font-weight: 800;
    font-size: 40px;
    letter-spacing: -0.5px;
  }
  /* Front side */
  .card-front {
    left: 300px;
    top: 470px;
    background: var(--paper);
  }
  .front-pattern {
    position: absolute;
    left: 150px; top: 20px; right: 20px; bottom: 60px;
    background: linear-gradient(135deg, var(--paper), var(--line-grey) 50%, var(--paper));
  }
  .front-wordmark {
    position: absolute;
    right: 40px;
    top: 26px;
    color: var(--navy);
    font-weight: 800;
    font-size: 78px;
    line-height: 1;
    letter-spacing: -1px;
  }
  .name-band {
    position: absolute;
    left: 0;
    top: 150px;
    width: 270px;
    height: 40px;
    background: var(--navy);
    color: var(--paper);
    font-weight: 600;
    font-size: 22px;
    letter-spacing: 0.5px;
    padding-left: 40px;
    line-height: 40px;
  }
  .job-title {
    position: absolute;
    left: 40px;
    top: 196px;
    font-size: 14px;
    color: var(--ink);
  }
  .website {
    position: absolute;
    right: 40px;
    top: 170px;
    font-size: 16px;
    letter-spacing: 1px;
    color: var(--ink);
  }
  .contact-list {
    position: absolute;
    left: 40px;
    bottom: 26px;
    list-style: none;
  }
  .contact-item {
    display: flex;
    align-items: center;
    gap: 8px;
    font-size: 16px;
    color: var(--ink);
    line-height: 24px;
  }
  .contact-item.phone { font-weight: 800; font-size: 17px; }
  .contact-icon { width: 14px; height: 14px; fill: var(--navy); }
</style>
</head>
<body>
  <section class="card card-back" aria-label="Business card back">
    <div class="back-pattern" role="img" aria-label="Repeated faint brand name pattern on navy"></div>
    <div class="back-wordmark">Vantry</div>
  </section>

  <section class="card card-front" aria-label="Business card front">
    <div class="front-pattern" role="img" aria-label="Faint line icons of charts, money and search tools"></div>
    <div class="front-wordmark">Vantry</div>
    <div class="name-band">MARCUS HALE</div>
    <div class="job-title">Managing Director</div>
    <div class="website">www.vantry.com</div>
    <ul class="contact-list">
      <li class="contact-item phone">
        <svg class="contact-icon" viewBox="0 0 16 16" aria-hidden="true"><path d="M2 5c0-2 2-3 3-3h6c1 0 3 1 3 3v1h-3V5H5v1H2z M4 7h8l2 6H2z M8 9a1.5 1.5 0 1 0 0 3a1.5 1.5 0 1 0 0-3z"/></svg>
        000-555-0142
      </li>
      <li class="contact-item email">
        <svg class="contact-icon" viewBox="0 0 16 16" aria-hidden="true"><path d="M1 3h14v10H1z" fill="none" stroke="#141c48" stroke-width="1.6"/><path d="M1 3l7 6l7-6" fill="none" stroke="#141c48" stroke-width="1.6"/></svg>
        info@vantrymail.com
      </li>
    </ul>
  </section>
</body>
</html>
```